Need Business Cards for my Business

email address: rkpmarlowhollowworks@vendrimail.com
web address: rkpmarlowhollowworks.net
Slogan: We offer various QVN licenses
Rowland K. Pemberly
Please stick with colors of Company Logo
would like the card to be more of the color example of the logo.
If you need PDF copy of logo email me at the above account.
Creative control rests with you.

Industry/Entity Type

Business

Contact Information for Business Card

I am a minimalist, but would like something to pop and stand out amongst other cards, make it memorable.

Font styles to use
Serif
Decorative
Script

```html
<!DOCTYPE html>
<html lang="en">
<head>
<meta charset="utf-8">
<title>Marlow Hollow Works – Business Cards</title>
<link rel="stylesheet" href="https://fonts.googleapis.com/css2?family=Montserrat:wght@400;600;700;800&display=swap">
<style>
  :root {
    --stage: #1c1c1c;
    --blue-light: #1f6fb0;
    --blue-dark: #183f6e;
    --navy-text: #1d2c45;
    --red: #e52a2f;
    --white: #ffffff;
  }
  * { box-sizing: border-box; margin: 0; padding: 0; }
  html, body {
    width: 1200px; height: 741px; overflow: hidden;
    background: var(--stage);
    font-family: "Montserrat", sans-serif;
  }
  .stage { position: relative; width: 1200px; height: 741px; }
  .card {
    position: absolute; top: 229px;
    width: 495px; height: 282px;
    box-shadow: 0 6px 18px rgba(0,0,0,.6);
    overflow: hidden;
  }
  .card--front { left: 98px; }
  .card--back { left: 608px; }
  .card__art { position: absolute; inset: 0; width: 100%; height: 100%; }
  .brand-name {
    position: absolute;
    font-weight: 800;
    color: var(--blue-dark);
    letter-spacing: 1px;
    line-height: 1;
    white-space: nowrap;
  }
  .card--front .brand-name {
    left: 0; right: 0; top: 118px; text-align: center; font-size: 27px;
    padding-left: 10px;
  }
  .card--back .brand-name {
    right: 34px; top: 52px; font-size: 24px;
  }
  .slogan {
    position: absolute; right: 37px; top: 110px;
    font-size: 12px; color: var(--red); letter-spacing: 1.6px;
  }
  .person {
    position: absolute; left: 21px; top: 172px;
    font-size: 15.5px; font-weight: 700; color: var(--navy-text);
  }
  .contact-list { position: absolute; left: 21px; top: 216px; list-style: none; }
  .contact-list li {
    display: flex; align-items: center; gap: 6px;
    font-size: 12.5px; font-weight: 600; color: var(--navy-text);
    height: 17px;
  }
  .contact-icon { width: 13px; height: 13px; flex: none; }
</style>
</head>
<body>
<main class="stage">
  <section class="card card--front" aria-label="Card front">
    <svg class="card__art" viewBox="0 0 600 342" preserveAspectRatio="none" aria-hidden="true">
      <defs>
        <linearGradient id="band-front" x1="0" y1="0" x2="0" y2="1">
          <stop offset="0" stop-color="var(--blue-light)"/>
          <stop offset="1" stop-color="var(--blue-dark)"/>
        </linearGradient>
      </defs>
      <rect width="600" height="342" fill="url(#band-front)"/>
      <path fill="var(--white)" d="M0,8 C150,2 250,0 330,8 C450,25 550,80 600,132 L600,320 C500,323 450,322 400,318 C250,302 80,245 0,140 Z"/>
    </svg>
    <div class="brand-name">MARLOW HOLLOW WORKS</div>
  </section>

  <section class="card card--back" aria-label="Card back">
    <svg class="card__art" viewBox="0 0 600 342" preserveAspectRatio="none" aria-hidden="true">
      <defs>
        <linearGradient id="band-back" x1="0" y1="0" x2="0" y2="1">
          <stop offset="0" stop-color="var(--blue-light)"/>
          <stop offset="1" stop-color="var(--blue-dark)"/>
        </linearGradient>
      </defs>
      <rect width="600" height="342" fill="url(#band-back)"/>
      <path fill="var(--white)" d="M0,130 C60,70 180,20 300,8 C420,0 520,4 600,8 L600,138 C540,230 400,318 200,322 C120,323 60,320 0,318 Z"/>
    </svg>
    <div class="brand-name">MARLOW HOLLOW WORKS</div>
    <p class="slogan">We offer various QVN licenses</p>
    <h1 class="person">ROWLAND K. PEMBERLY</h1>
    <ul class="contact-list">
      <li>
        <svg class="contact-icon" viewBox="0 0 14 14" aria-hidden="true">
          <rect width="14" height="14" rx="2" fill="var(--red)"/>
          <rect x="2.5" y="4" width="9" height="6.5" fill="none" stroke="#fff" stroke-width="1.1"/>
          <path d="M2.5 4 L7 8 L11.5 4" fill="none" stroke="#fff" stroke-width="1.1"/>
        </svg>
        rkpmarlowhollowworks@vendrimail.com
      </li>
      <li>
        <svg class="contact-icon" viewBox="0 0 14 14" aria-hidden="true">
          <rect width="14" height="14" rx="2" fill="var(--red)"/>
          <circle cx="7" cy="7" r="4.3" fill="none" stroke="#fff" stroke-width="1"/>
          <ellipse cx="7" cy="7" rx="1.9" ry="4.3" fill="none" stroke="#fff" stroke-width="0.9"/>
          <path d="M2.7 7 H11.3" stroke="#fff" stroke-width="0.9"/>
        </svg>
        rkpmarlowhollowworks.net
      </li>
    </ul>
  </section>
</main>
</body>
</html>
```